DM - management consultant

Business card - contemporary design

Front info
Dorian Maples

(Address not necessary)
PO Box 7386
Belmont, CA 94002

(650) 555-0143
dm@dorianmapl.es

Twitter: dmq527
Facebook: /Dorian.Maples
Linkedin: /in/dorianmaples

Back or Front
www.dorianmaples.net
Facilitation & coaching, change management, strategic partnerships, business improvement

Target Market(s)

High tech businesses - mostly startups in Silicon Valley

Industry/Entity Type

Business

Font styles to use
Sans Serif

Colors

Designer to choose colors to be used in the design.

```html
<!DOCTYPE html>
<html lang="en">
<head>
<meta charset="utf-8">
<title>Dorian Maples – Business Card</title>
<link rel="stylesheet" href="https://fonts.googleapis.com/css2?family=Arimo:wght@400&display=swap">
<style>
  :root {
    --red-bright: #e81d25;
    --red-deep: #c9372c;
    --red-muted: #b9705f;
    --mist: #d9d2d3;
    --peach-soft: rgba(246, 214, 200, 0.55);
    --peach-pale: rgba(252, 238, 232, 0.85);
    --ink: #333333;
    --url-red: #e0332a;
    --white: #ffffff;
    --phone-tint: #f0d6d4;
    --divider: #222222;
    --icon-grey: #555555;
  }
  * { margin: 0; padding: 0; box-sizing: border-box; }
  html, body {
    width: 1200px; height: 343px; overflow: hidden;
    background: var(--white);
    font-family: "Arimo", Arial, sans-serif;
  }
  .card { position: relative; width: 1200px; height: 343px; }

  .card-front {
    position: absolute; left: 0; top: 0; width: 600px; height: 343px; overflow: hidden;
    background: linear-gradient(90deg, var(--red-bright) 0%, var(--red-deep) 40%, var(--red-muted) 70%, var(--mist) 100%);
  }
  .front-motif {
    position: absolute; left: 290px; top: 0; width: 310px; height: 343px;
    background:
      linear-gradient(180deg, rgba(255,255,255,0.08) 0%, var(--peach-soft) 60%, var(--peach-pale) 100%),
      linear-gradient(90deg, rgba(255,255,255,0) 0%, rgba(255,255,255,0.35) 100%);
  }
  .fold-line {
    position: absolute; left: 599px; top: 0; height: 343px;
    border-left: 1.5px dotted var(--divider);
  }
  .name, .phone, .title, .service {
    position: absolute; white-space: nowrap; line-height: 1; font-weight: 400;
  }
  .name { left: 32px; top: 26px; font-size: 29px; color: var(--white); }
  .phone { left: 294px; top: 28px; font-size: 27px; color: var(--phone-tint); opacity: .9; }
  .title { left: 33px; top: 70px; font-size: 13px; color: var(--white); }
  .services { list-style: none; }
  .service { left: 32px; font-size: 22px; color: var(--white); }
  .service:nth-child(1) { top: 138px; }
  .service:nth-child(2) { top: 178px; }
  .service:nth-child(3) { top: 218px; }
  .service:nth-child(4) { top: 265px; }

  .card-back { position: absolute; left: 601px; top: 0; width: 599px; height: 343px; }
  .website {
    position: absolute; left: 0; width: 100%; top: 137px;
    text-align: center; font-size: 30px; color: var(--url-red); line-height: 1;
  }
  .email {
    position: absolute; left: 0; width: 100%; top: 266px;
    text-align: center; font-size: 20px; color: var(--ink); line-height: 1;
  }
  .profile {
    position: absolute; left: 141px; top: 293px;
    display: flex; align-items: center; gap: 7px;
    font-size: 20px; color: var(--ink); line-height: 1;
  }
  .profile-square { width: 34px; height: 34px; background: var(--icon-grey); border-radius: 3px; }
</style>
</head>
<body>
<main class="card">
  <section class="card-front">
    <div class="front-motif" role="img" aria-label="Decorative rising-steps motif in soft peach tones"></div>
    <h1 class="name">Dorian Maples</h1>
    <p class="phone">(650) 555-0143</p>
    <p class="title">Management Consultant</p>
    <ul class="services">
      <li class="service">Facilitation &amp; Coaching</li>
      <li class="service">Business Improvement</li>
      <li class="service">Change Management</li>
      <li class="service">Strategic Partnerships</li>
    </ul>
  </section>
  <div class="fold-line"></div>
  <section class="card-back">
    <p class="website">www.dorianmaples.net</p>
    <p class="email">dm@dorianmapl.es</p>
    <p class="profile"><span class="profile-square"></span>proflink.net/in/dorianmaples</p>
  </section>
</main>
</body>
</html>
```